Elegant Black Candle Label Design!

I need a 2.375" tall by 3.0" wide candle label design. I'm looking for simple and elegant. Black label with silver leaf border and lettering. Label needs to have the following information on it: Fern Hollow Candle Co. as the company name, scent name in the middle and in smaller font, it needs to say Made in USA, All Natural, 8oz. Attached photos are for inspiration.

Target Market(s)

People looking for high end, all natural candle fragrances

Industry/Entity Type

Candle-Spa

Colors

Designer to choose only greyscale colors for use in the design.

Requirements
Must have
• Company Name, Scent (ability to change scent names), All Natural, Made in USA, 8oz
Nice to have
• Black background, silver leaf border and silver leaf font. Elegant fonts maybe slightly cursive

```html
<!DOCTYPE html>
<html lang="en">
<head>
<meta charset="UTF-8">
<title>Fern Hollow Candle Co. – Soy Candle Label</title>
<link href="https://fonts.googleapis.com/css2?family=Marcellus&display=swap" rel="stylesheet">
<style>
  :root {
    --backdrop: #2e2e2e;
    --label-black: #202020;
    --silver: #d9d9d9;
    --silver-light: #f4f4f4;
    --silver-dark: #9a9a9a;
  }
  * { margin: 0; padding: 0; box-sizing: border-box; }
  html, body {
    width: 1200px;
    height: 960px;
    overflow: hidden;
    background: var(--backdrop);
  }
  .label {
    position: absolute;
    left: 50px;
    top: 45px;
    width: 1100px;
    height: 870px;
    background: var(--label-black);
    font-family: "Marcellus", serif;
    color: var(--silver);
  }
  .label__frame {
    position: absolute;
    left: 0;
    top: 0;
    width: 1100px;
    height: 870px;
  }
  .label__brand {
    position: absolute;
    left: 0;
    right: 0;
    top: 250px;
    text-align: center;
    font-size: 62px;
    letter-spacing: 3px;
    color: var(--silver);
  }
  .label__scent {
    position: absolute;
    left: 0;
    right: 0;
    top: 468px;
    text-align: center;
    font-size: 40px;
    letter-spacing: 3px;
    color: var(--silver);
  }
  .label__scent-rule {
    position: absolute;
    left: 210px;
    top: 530px;
    width: 680px;
    height: 3px;
    background: linear-gradient(90deg, var(--silver-dark), var(--silver-light) 50%, var(--silver-dark));
  }
  .label__details {
    position: absolute;
    left: 190px;
    right: 190px;
    top: 668px;
    display: flex;
    justify-content: space-between;
    font-size: 26px;
    letter-spacing: 1px;
    color: var(--silver);
  }
</style>
</head>
<body>
  <main class="label">
    <svg class="label__frame" viewBox="0 0 1100 870" aria-hidden="true">
      <defs>
        <linearGradient id="silver-leaf" x1="0" y1="0" x2="1" y2="1">
          <stop offset="0" stop-color="#a8a8a8"/>
          <stop offset="0.45" stop-color="#f5f5f5"/>
          <stop offset="0.7" stop-color="#bdbdbd"/>
          <stop offset="1" stop-color="#e8e8e8"/>
        </linearGradient>
      </defs>
      <rect x="68" y="68" width="964" height="734" fill="none" stroke="url(#silver-leaf)" stroke-width="4"/>
    </svg>

    <h1 class="label__brand">Fern Hollow Candle Co.</h1>

    <h2 class="label__scent">SOY CANDLE</h2>
    <div class="label__scent-rule"></div>

    <div class="label__details">
      <span class="label__detail">ALL NATURAL</span>
      <span class="label__detail">8OZ</span>
      <span class="label__detail">MADE IN USA</span>
    </div>
  </main>
</body>
</html>
```